CalmHarbor Homepage and Landing Pages

Please see detailed brief.

CalmHarbor is Australia’s newest online therapy and mental health service. We allow patients from across australia to connect with Mental health practitioners from across Australia. Our mission is to remove the friction in gaining support for mental health related issues.

Number of Pages Required

1 page

Font styles to use
Sans Serif

Colors
33a6d7
0293ce
3277b5
0255a3
acd136
9bcb3c

Requirements
Must have
• Please see detailed brief.
Nice to have
• Please see detailed brief
Should not have

```html
<!DOCTYPE html>
<html lang="en">
<head>
<meta charset="utf-8">
<title>CalmHarbor – Online Therapy &amp; Mental Health</title>
<link href="https://fonts.googleapis.com/css2?family=Raleway:wght@400;500;600;700&family=Mulish:ital,wght@0,400;0,600;0,700;1,400&display=swap" rel="stylesheet">
<style>
:root{
  --sky:#33a6d7;
  --blue:#0293ce;
  --mid:#3277b5;
  --navy:#0255a3;
  --ink:#3a3a3a;
  --text:#666;
  --soft:#f3f4f6;
  --dark:#2b2e33;
  --line:#d8d8d8;
}
*{margin:0;padding:0;box-sizing:border-box}
html,body{width:1200px;height:3428px;overflow:hidden}
body{position:relative;background:#fff;font-family:'Mulish',sans-serif;color:var(--text);font-size:11px}
.abs{position:absolute}
h1,h2,h3,h4,.brand{font-family:'Raleway',sans-serif}

/* header */
.topbar{left:600px;top:0;width:600px;height:29px;background:var(--sky)}
.topbar-links{left:776px;top:7px;color:#fff;font-size:10px}
.topbar-links span{margin-right:12px}
.book-btn{left:885px;top:0;width:151px;height:29px;background:var(--navy);color:#fff;font-size:11.5px;font-weight:600;display:flex;align-items:center;justify-content:center}
.header{left:0;top:29px;width:1200px;height:46px;background:#fff;border-bottom:1px solid #eee}
.brand{display:flex;align-items:center;gap:8px;color:#3d3d3d;font-weight:500}
.brand .dot{width:22px;height:22px;border-radius:50%;background:var(--blue)}
.brand-head{left:162px;top:20px;font-size:30px}
.nav{left:567px;top:46px;display:flex;gap:19px;font-size:11.5px;color:#555}
.nav .on{color:var(--blue)}

/* hero */
.hero-photo{left:0;top:0}
.hero-title{left:162px;top:176px;font-size:52px;font-weight:600;color:var(--blue);letter-spacing:1px}
.hero-sub{left:162px;top:243px;width:360px;font-size:11.5px;color:var(--blue);font-weight:600;line-height:17px}
.hero-copy{left:162px;top:293px;width:370px;font-size:11.5px;line-height:17px;color:#555}
.btn{background:var(--navy);color:#fff;font-size:11px;font-weight:700;display:flex;align-items:center;justify-content:center;border-radius:2px}
.hero-btn{left:162px;top:359px;width:92px;height:26px}

/* section titles */
.sec-title{left:0;width:1200px;text-align:center;font-size:20px;font-weight:600;color:#444}
.sec-title b{color:var(--navy);font-weight:700}
.sec-title.light{color:#fff}
.sec-title.light b{color:var(--sky)}
.divider{left:510px;width:180px;height:14px}

/* services */
.service{width:240px;text-align:center}
.service .ico{width:40px;height:40px;margin:0 auto;border-radius:50%;border:2px solid var(--blue);background:#e8f5fb}
.service h3{margin-top:12px;font-size:12px;font-weight:700;color:#333;letter-spacing:.5px}
.service .bar{width:22px;height:2px;background:var(--navy);margin:6px auto 8px}
.service p{font-size:11px;line-height:15px;color:#666}

/* about */
.about-title{left:540px;top:1138px;width:460px;font-size:16px;font-weight:700;color:var(--mid);line-height:20px;letter-spacing:.5px}
.about-copy{left:540px;top:1184px;width:500px;font-size:11px;line-height:15px;color:#666}
.about-copy p{margin-bottom:15px}
.about-btn{left:540px;top:1382px;width:107px;height:25px}

/* team */
.member{width:196px;height:221px;top:1583px}
.member .photo{width:196px;height:221px}
.plate{width:166px;height:67px;top:1772px;background:#fff;box-shadow:0 1px 4px rgba(0,0,0,.18);text-align:center;padding-top:26px}
.plate h4{font-size:12.5px;color:var(--navy);font-weight:600}
.plate p{font-size:10px;font-style:italic;color:#888;margin-top:2px}
.socials{display:flex;gap:8px}
.socials i{display:block;width:21px;height:21px;border-radius:50%;background:var(--navy)}
.overlay{background:#2d3035;color:#fff;text-align:center;padding:26px 12px 0}
.overlay h4{font-size:12.5px;color:var(--navy);font-weight:600}
.overlay em{display:block;font-size:10px;margin-top:2px}
.overlay p{font-size:10.5px;line-height:13.5px;margin-top:16px}

/* testimonial */
.avatar{left:559px;top:2042px;width:82px;height:83px;border:3px solid #fff;box-shadow:0 1px 5px rgba(0,0,0,.2);background:linear-gradient(#7fc4ea,#3a9fd9)}
.quote{left:197px;top:2141px;width:807px;text-align:center;font-size:11px;line-height:15px;color:#777}
.client{left:0;top:2210px;width:1200px;text-align:center;font-size:13px;font-weight:600;color:var(--blue)}
.client-role{left:0;top:2229px;width:1200px;text-align:center;font-size:9px;font-style:italic;color:#999}
.dots{left:544px;top:2258px;display:flex;gap:8px}
.dots i{display:block;width:32px;height:6px;border-radius:3px;border:1px solid #bbb}
.dots i.on{border-color:var(--sky);background:#e4f3fa}

/* blog */
.post{top:2452px;width:271px;height:169px}
.post-card{top:2588px;width:248px;height:155px;background:#fff;box-shadow:0 1px 5px rgba(0,0,0,.15);padding:12px 12px}
.post-card h4{font-size:13.5px;color:#333;font-weight:500}
.post-card .meta{font-size:8.5px;color:#888;margin-top:3px;line-height:13px}
.post-card p{font-size:10px;line-height:14.5px;color:#888;margin-top:10px}
.post-card .more{font-size:11.5px;font-weight:700;color:var(--blue);margin-top:6px}

/* appointment */
.appt-copy{left:0;top:2882px;width:1200px;text-align:center;font-size:11px;color:#fff}
.field{height:30px;border:1px solid #aaa;border-radius:3px;color:#ddd;font-size:11px;padding:9px 12px;background:rgba(255,255,255,.03)}
.submit{left:560px;top:3148px;width:87px;height:25px;background:var(--navy);color:#fff;font-size:11px;font-weight:700;display:flex;align-items:center;justify-content:center;border-radius:2px;letter-spacing:.5px}

/* footer */
.brand-foot{left:162px;top:3276px;font-size:28px;color:#fff}
.brand-foot .dot{background:#fff}
.foot-copy{left:162px;top:3319px;font-size:10px;line-height:14px;color:#fff}
.foot-social{left:162px;top:3360px;display:flex;gap:6px}
.foot-social i{display:block;width:19px;height:19px;border-radius:50%;border:1px solid rgba(255,255,255,.6)}
.foot-h{font-size:19px;color:#fff;font-weight:500;border-bottom:1px solid rgba(255,255,255,.8);padding-bottom:4px}
.foot-links{font-size:10px;color:#fff;line-height:22.5px}
.foot-links li{list-style:none;padding-left:12px;position:relative}
.foot-links li::before{content:"";position:absolute;left:0;top:9px;width:5px;height:5px;border:1px solid #fff;border-radius:50%}
.contact-row{display:flex;gap:10px;align-items:flex-start;color:#fff;font-size:10.5px;line-height:14px}
</style>
</head>
<body>

<!-- hero photo -->
<svg class="abs hero-photo" width="1200" height="560" role="img" aria-label="Physiotherapist stretching a patient's leg on a treatment table in a bright clinic">
  <defs>
    <linearGradient id="heroG" x1="0" y1="0" x2="1" y2="1">
      <stop offset="0" stop-color="#e9eef1"/>
      <stop offset=".5" stop-color="#9aa7b0"/>
      <stop offset="1" stop-color="#c9d2d8"/>
    </linearGradient>
  </defs>
  <path d="M460 0 C520 120 560 190 578 330 C596 470 680 540 820 526 C960 512 1080 470 1200 468 L1200 0 Z" fill="url(#heroG)"/>
  <path d="M700 530 C820 535 900 510 1000 498 C1090 488 1150 482 1200 486" fill="none" stroke="var(--navy)" stroke-width="6"/>
</svg>

<div class="abs topbar"></div>
<div class="abs topbar-links"><span>Login</span><span>Register</span></div>
<div class="abs book-btn">Book An Appointment</div>
<div class="abs header"></div>
<div class="abs brand brand-head"><span class="dot"></span>CalmHarbor</div>
<nav class="abs nav"><span class="on">Home</span><span>About Us</span><span>Services</span><span>Practitioner Information</span><span>Our Team</span><span>Contact Us</span></nav>

<h1 class="abs hero-title">CalmHarbor</h1>
<p class="abs hero-sub">CalmHarbor is Australia's newest online therapy and mental health service.</p>
<p class="abs hero-copy">But I must explain to you how all this mistaken idea of denouncing pleasure and praising pain was born and I will give you a complete account of the system.</p>
<div class="abs btn hero-btn">Contact Us</div>

<!-- services -->
<h2 class="abs sec-title" style="top:582px">Our <b>Services</b></h2>
<svg class="abs divider" style="top:615px" viewBox="0 0 180 14"><line x1="0" y1="7" x2="78" y2="7" stroke="var(--line)"/><line x1="102" y1="7" x2="180" y2="7" stroke="var(--line)"/><circle cx="90" cy="7" r="6" fill="none" stroke="var(--blue)" stroke-width="2"/></svg>

<div class="abs service" style="left:189px;top:652px"><div class="ico" role="img" aria-label="Mental health icon"></div><h3>MENTAL HEALTH</h3><div class="bar"></div><p>But I must explain to you how all this mistaken idea of denouncing pleasure and praising pain was born complete...</p></div>
<div class="abs service" style="left:480px;top:652px"><div class="ico" role="img" aria-label="Physical therapy icon"></div><h3>PHYSICAL THERAPY</h3><div class="bar"></div><p>But I must explain to you how all this mistaken idea of denouncing pleasure and praising pain was born complete...</p></div>
<div class="abs service" style="left:770px;top:652px"><div class="ico" role="img" aria-label="Family therapy icon"></div><h3>FAMILY THERAPY</h3><div class="bar"></div><p>But I must explain to you how all this mistaken idea of denouncing pleasure and praising pain was born complete...</p></div>
<div class="abs service" style="left:189px;top:811px"><div class="ico" role="img" aria-label="Pilates therapy icon"></div><h3>PILATES THERAPY</h3><div class="bar"></div><p>But I must explain to you how all this mistaken idea of denouncing pleasure and praising pain was born complete...</p></div>
<div class="abs service" style="left:480px;top:811px"><div class="ico" role="img" aria-label="Acupuncture icon"></div><h3>ACUPUNCTURE</h3><div class="bar"></div><p>But I must explain to you how all this mistaken idea of denouncing pleasure and praising pain was born complete...</p></div>
<div class="abs service" style="left:770px;top:811px"><div class="ico" role="img" aria-label="Herbal therapy icon"></div><h3>HERBAL THERAPY</h3><div class="bar"></div><p>But I must explain to you how all this mistaken idea of denouncing pleasure and praising pain was born complete...</p></div>

<!-- about band -->
<svg class="abs" style="left:0;top:950px" width="1200" height="520"><path d="M0 8 C300 40 600 80 820 70 C980 62 1100 40 1200 20 L1200 470 C1000 500 700 520 400 505 C200 495 80 480 0 470 Z" fill="var(--soft)"/></svg>
<h2 class="abs sec-title" style="top:1066px">Abutus <b>CalmHarbor</b></h2>
<svg class="abs divider" style="top:1099px" viewBox="0 0 180 14"><line x1="0" y1="7" x2="78" y2="7" stroke="var(--line)"/><line x1="102" y1="7" x2="180" y2="7" stroke="var(--line)"/><circle cx="90" cy="7" r="6" fill="none" stroke="var(--blue)" stroke-width="2"/></svg>

<svg class="abs" style="left:162px;top:1128px" width="346" height="278" role="img" aria-label="Two round photos: therapist treating a smiling patient's shoulder, and seniors exercising with dumbbells">
  <circle cx="128" cy="128" r="128" fill="#c9b8ad"/>
  <circle cx="128" cy="128" r="118" fill="none" stroke="#fff" stroke-dasharray="5 4"/>
  <circle cx="256" cy="188" r="90" fill="#a9b6c4" stroke="#fff" stroke-width="3"/>
  <circle cx="256" cy="188" r="80" fill="none" stroke="#fff" stroke-dasharray="5 4"/>
  <path d="M172 170 A90 90 0 0 0 232 275" fill="none" stroke="var(--navy)" stroke-width="4"/>
</svg>

<h3 class="abs about-title">PHYSIOTHERAPY SERVICES FROM PROFESSIONALS THERAPISTS</h3>
<div class="abs about-copy">
  <p>Sed ut perspiciatis unde omnis iste natus error sit voluptatem accusantium doloremque laudantium, totam rem aperiam, eaque ipsa quae ab illo inventore veritatis et quasi architecto beatae vitae dicta sunt explicabo.</p>
  <p>Lorem ipsum dolor sit amet, consectetur adipiscing elit, sed do eiusmod tempor incididunt ut labore et dolore magna aliqua. Ut enim ad minim veniam, quis nostrud exercitation ullamco laboris nisi ut aliquip ex ea commodo consequat. Duis aute irure dolor in reprehenderit in voluptate velit esse cillum dolore eu fugiat nulla pariatur.</p>
  <p>But I must explain to you how all this mistaken idea of denouncing pleasure and praising pain was born and I will give you a complete account of the system, and expound the actual teachings of the great explorer of the truth, the master-builder of human happiness.</p>
</div>
<div class="abs btn about-btn">More About Me</div>

<!-- team -->
<h2 class="abs sec-title" style="top:1508px">Our <b>Team</b></h2>
<svg class="abs divider" style="top:1541px" viewBox="0 0 180 14"><line x1="0" y1="7" x2="78" y2="7" stroke="var(--line)"/><line x1="102" y1="7" x2="180" y2="7" stroke="var(--line)"/><circle cx="90" cy="7" r="6" fill="none" stroke="var(--blue)" stroke-width="2"/></svg>

<div class="abs member" style="left:174px"><div class="photo" role="img" aria-label="Portrait of a doctor holding a blue folder" style="background:linear-gradient(#eef2f5,#d7dde2)"></div></div>
<div class="abs member overlay" style="left:392px" role="group">
  <h4>Owen R. Calder</h4><em>Lorem ipsum dolor sit amet</em>
  <p>Sed ut perspiciatis unde omnis iste natus error sit voluptatem accusantium doloremque laudantium, totam rem aperiam, eaque ipsa vitae dicta sunt explicabo.</p>
  <div class="socials" style="justify-content:center;margin-top:14px"><i></i><i></i><i></i><i></i></div>
</div>
<div class="abs member" style="left:609px"><div class="photo" role="img" aria-label="Portrait of a smiling doctor with a stethoscope" style="background:linear-gradient(#ffffff,#e6e3e1)"></div></div>
<div class="abs member" style="left:829px"><div class="photo" role="img" aria-label="Portrait of a senior doctor in a white coat" style="background:linear-gradient(#dfe4e7,#bfc8cf)"></div></div>

<div class="abs plate" style="left:189px"><h4>Mara T. Holloway</h4><p>Lorem ipsum dolor sit amet</p></div>
<div class="abs socials" style="left:215px;top:1761px"><i></i><i></i><i></i><i></i></div>
<div class="abs plate" style="left:625px"><h4>Lena S. Varga</h4><p>Lorem ipsum dolor sit amet</p></div>
<div class="abs socials" style="left:652px;top:1761px"><i></i><i></i><i></i><i></i></div>
<div class="abs plate" style="left:844px"><h4>Victor M. Hale</h4><p>Lorem ipsum dolor sit amet</p></div>
<div class="abs socials" style="left:871px;top:1761px"><i></i><i></i><i></i><i></i></div>

<!-- testimonial band -->
<svg class="abs" style="left:0;top:1860px" width="1200" height="500"><path d="M0 10 C200 60 420 100 700 96 C900 94 1080 70 1200 50 L1200 470 C1000 490 800 480 600 470 C400 462 200 470 0 480 Z" fill="var(--soft)"/></svg>
<h2 class="abs sec-title" style="top:1976px">Happy Client <b>are Saying</b></h2>
<svg class="abs divider" style="top:2009px" viewBox="0 0 180 14"><line x1="0" y1="7" x2="78" y2="7" stroke="var(--line)"/><line x1="102" y1="7" x2="180" y2="7" stroke="var(--line)"/><circle cx="90" cy="7" r="6" fill="none" stroke="var(--blue)" stroke-width="2"/></svg>
<div class="abs avatar" role="img" aria-label="Client avatar illustration"></div>
<p class="abs quote">Sed ut perspiciatis unde omnis iste natus error sit voluptatem accusantium doloremque laudantium, totam rem aperiam, eaque ipsa quae ab illo inventore veritatis et quasi architecto beatae vitae dicta sunt explicabo. Nemo enim ipsam voluptatem quia voluptas sit aspernatur aut odit aut fugit, sed quia consequuntur magni dolores eos qui ratione voluptatem sequi nesciunt. Neque porro quisquam est, qui dolorem ipsum quia dolor sit amet.</p>
<div class="abs client">PETER LINDQVIST</div>
<div class="abs client-role">LOREM IPSUM DOLOR SIT AMET</div>
<div class="abs dots"><i></i><i class="on"></i><i></i></div>

<!-- blog -->
<h2 class="abs sec-title" style="top:2382px">Latest <b>Blog</b></h2>
<svg class="abs divider" style="top:2415px" viewBox="0 0 180 14"><line x1="0" y1="7" x2="78" y2="7" stroke="var(--line)"/><line x1="102" y1="7" x2="180" y2="7" stroke="var(--line)"/><circle cx="90" cy="7" r="6" fill="none" stroke="var(--blue)" stroke-width="2"/></svg>

<div class="abs post" style="left:173px;background:linear-gradient(#e9ecef,#c8cfd4)" role="img" aria-label="Doctor checking an elderly patient with a stethoscope"></div>
<div class="abs post" style="left:464px;background:linear-gradient(#d6e4ee,#8fa9bb)" role="img" aria-label="Patient doing physical therapy on an exercise ball"></div>
<div class="abs post" style="left:754px;background:linear-gradient(#ede9e6,#b9b3ae)" role="img" aria-label="Therapist treating a patient's shoulder"></div>

<div class="abs post-card" style="left:184px"><h4>Health Checkup Body</h4><div class="meta">Posted by Nora Ellison<br>Jan 15, 2020 &nbsp;/&nbsp; Leave a Comment</div><p>Lorem ipsum dolor sit amet, consectetur adipiscing elit, sed do eiusmod tempor incididunt ut labore et dolore...</p><div class="more">Read More &nbsp;»</div></div>
<div class="abs post-card" style="left:475px"><h4>Physical Therapy</h4><div class="meta">Posted by Nora Ellison<br>Jan 25, 2020 &nbsp;/&nbsp; Leave a Comment</div><p>Lorem ipsum dolor sit amet, consectetur adipiscing elit, sed do eiusmod tempor incididunt ut labore et dolore...</p><div class="more">Read More &nbsp;»</div></div>
<div class="abs post-card" style="left:765px"><h4>Lorem ipsum dolor sit amet</h4><div class="meta">Posted by Nora Ellison<br>Jan 26, 2020 &nbsp;/&nbsp; Leave a Comment</div><p>Lorem ipsum dolor sit amet, consectetur adipiscing elit, sed do eiusmod tempor incididunt ut labore et dolore...</p><div class="more">Read More &nbsp;»</div></div>

<!-- appointment -->
<div class="abs" style="left:0;top:2804px;width:1200px;height:624px;background:linear-gradient(135deg,#3a3d42,#24272b 60%,#2f3a45)" role="img" aria-label="Blurred clinic background photo"></div>
<h2 class="abs sec-title light" style="top:2826px;letter-spacing:1px">BOOK AN <b>APPOINTMENT</b></h2>
<svg class="abs divider" style="top:2858px" viewBox="0 0 180 14"><line x1="0" y1="7" x2="78" y2="7" stroke="#666"/><line x1="102" y1="7" x2="180" y2="7" stroke="#666"/><circle cx="90" cy="7" r="6" fill="none" stroke="var(--sky)" stroke-width="2"/></svg>
<p class="abs appt-copy">Sed ut perspiciatis unde omnis iste natus error sit voluptatem accusantium doloremque laudantium</p>
<div class="abs field" style="left:353px;top:2921px;width:239px">First Name</div>
<div class="abs field" style="left:607px;top:2921px;width:240px">Email Address</div>
<div class="abs field" style="left:353px;top:2963px;width:239px">Your Subject</div>
<div class="abs field" style="left:607px;top:2963px;width:240px">Phone</div>
<div class="abs field" style="left:353px;top:3005px;width:239px">Appointment Date</div>
<div class="abs field" style="left:607px;top:3005px;width:240px">Appointment Time</div>
<div class="abs field" style="left:353px;top:3047px;width:494px;height:84px">Message</div>

<!-- footer -->
<svg class="abs" style="left:0;top:3130px" width="1200" height="298">
  <path d="M0 20 C200 80 500 100 800 95 C950 92 1080 80 1200 70 L1200 298 L0 298 Z" fill="var(--sky)"/>
  <path d="M0 80 C300 60 600 90 900 110 C1030 120 1130 110 1200 100 L1200 298 L0 298 Z" fill="var(--blue)"/>
  <path d="M950 298 C1050 250 1130 200 1200 190 L1200 298 Z" fill="var(--navy)" opacity=".6"/>
</svg>
<div class="abs submit">SUBMIT</div>

<div class="abs brand brand-foot"><span class="dot"></span>CalmHarbor</div>
<p class="abs foot-copy">Copyright © 2020 CalmHarbor.<br>All Right Reserved.</p>
<div class="abs foot-social"><i></i><i></i><i></i><i></i><i></i></div>

<h4 class="abs foot-h" style="left:468px;top:3268px;width:150px">Important Links</h4>
<ul class="abs foot-links" style="left:468px;top:3311px"><li>Home</li><li>Services</li><li>Our Team</li><li>Term &amp; Condition</li></ul>
<ul class="abs foot-links" style="left:603px;top:3311px"><li>About Us</li><li>Practitioner Information</li><li>Contact Us</li><li>Privacy Policy</li></ul>

<h4 class="abs foot-h" style="left:799px;top:3268px;width:185px">Contact Information</h4>
<div class="abs contact-row" style="left:803px;top:3316px">
  <svg width="14" height="20" viewBox="0 0 14 20"><path d="M7 1a6 6 0 0 1 6 6c0 4.5-6 12-6 12S1 11.5 1 7a6 6 0 0 1 6-6z" fill="none" stroke="#fff"/><circle cx="7" cy="7" r="2.2" fill="none" stroke="#fff"/></svg>
  <span>48 Harbour Crescent,<br>Seacliff, NSW 2099</span>
</div>
<div class="abs contact-row" style="left:801px;top:3362px">
  <svg width="17" height="17" viewBox="0 0 17 17"><path d="M4 1.5l2.5 3-1.6 1.8c.9 2 2.5 3.6 4.5 4.5l1.8-1.6 3 2.5-1.4 2.6c-5.5-.4-10.4-5.3-10.8-10.8z" fill="none" stroke="#fff"/></svg>
  <span style="padding-top:2px">(02) 5550 1842</span>
</div>
<div class="abs contact-row" style="left:801px;top:3393px">
  <svg width="18" height="14" viewBox="0 0 18 14"><rect x=".5" y=".5" width="17" height="13" fill="none" stroke="#fff"/><path d="M.5 .5l8.5 7 8.5-7" fill="none" stroke="#fff"/></svg>
  <span>hello@calmharbor.example</span>
</div>

</body>
</html>
```